Business Card Design needed for logo design project

This project is linked to Crisp Lane Glow logo refresh..

Our company needs a Business Card Design. Please refer to our original project in the link above.

```html
<!DOCTYPE html>
<html lang="en">
<head>
<meta charset="utf-8">
<title>Crisp Lane Glow — Business Card</title>
<link rel="stylesheet" href="https://fonts.googleapis.com/css2?family=Open+Sans:wght@300;400;600&display=swap">
<style>
  :root {
    --page-bg: #e6e4e0;
    --card-white: #ffffff;
    --card-shade: #f1f1f1;
    --ink: #4a4a4a;
    --ink-soft: #6a6a6a;
    --accent-blue: #3aaedf;
    --brand-blue: #2f9fd4;
    --icon-ink: #555555;
  }
  * { margin: 0; padding: 0; box-sizing: border-box; }
  html, body {
    width: 1200px; height: 1023px; overflow: hidden;
    background: var(--page-bg);
    font-family: "Open Sans", Arial, sans-serif;
    color: var(--ink);
  }
  .canvas {
    position: relative; width: 1200px; height: 1023px;
  }
  .business-card {
    position: absolute; left: 75px; top: 211px;
    width: 1050px; height: 600px;
    background: linear-gradient(160deg, var(--card-white) 0%, var(--card-white) 55%, var(--card-shade) 100%);
    box-shadow: 0 8px 28px rgba(0,0,0,0.18);
  }
  .identity {
    position: absolute; right: 230px; top: 56px;
    text-align: right; font-weight: 300;
  }
  .identity .person-name { font-size: 36px; line-height: 1.2; }
  .identity .person-title { font-size: 30px; line-height: 1.2; color: var(--ink-soft); }

  .brand-mark {
    position: absolute; left: 80px; top: 250px;
    display: flex; align-items: center; gap: 18px;
  }
  .brand-mark .brand-dot {
    width: 44px; height: 44px; border-radius: 50%;
    background: var(--brand-blue);
  }
  .brand-mark .brand-name {
    font-size: 52px; font-weight: 600; color: var(--brand-blue);
    letter-spacing: 0.5px;
  }

  .contact-list {
    position: absolute; right: 48px; top: 172px;
    list-style: none; font-size: 27px; font-weight: 400;
  }
  .contact-list li {
    display: flex; justify-content: flex-end; align-items: center;
    gap: 16px; height: 38px;
  }
  .contact-list li.gap-before { margin-top: 32px; }
  .contact-list svg { width: 22px; height: 22px; flex: none; }

  .accent-rule {
    position: absolute; left: 0; right: 0; top: 468px;
    height: 3px; background: var(--accent-blue);
  }
  .tagline, .service-area {
    position: absolute; top: 484px;
    font-size: 34px; font-weight: 300; color: var(--ink-soft);
  }
  .tagline { left: 34px; }
  .service-area { right: 60px; font-size: 30px; }
</style>
</head>
<body>
<main class="canvas">
  <section class="business-card" aria-label="Crisp Lane Glow business card">
    <div class="identity">
      <p class="person-name">Mark Ellison</p>
      <p class="person-title">President</p>
    </div>

    <div class="brand-mark">
      <span class="brand-dot"></span>
      <span class="brand-name">Crisp Lane Glow</span>
    </div>

    <ul class="contact-list">
      <li>off:555-310-4821
        <svg viewBox="0 0 24 24" aria-hidden="true"><circle cx="12" cy="12" r="11" fill="var(--icon-ink)"/><path d="M8 6c1 0 2 2.5 2 3s-1 1-1 1.5 2 3.5 4.5 4.5c.5 0 1-1 1.5-1s3 1 3 2-1.5 2.5-2.5 2.5C10 18.5 5.5 14 5.5 8.5 5.5 7.5 7 6 8 6z" fill="#fff"/></svg>
      </li>
      <li>555-310-4836
        <svg viewBox="0 0 24 24" aria-hidden="true"><rect x="3" y="10" width="18" height="11" rx="1.5" fill="none" stroke="var(--icon-ink)" stroke-width="1.8"/><rect x="7" y="3" width="10" height="7" fill="none" stroke="var(--icon-ink)" stroke-width="1.8"/><path d="M7 14h10M7 17h6" stroke="var(--icon-ink)" stroke-width="1.6"/></svg>
      </li>
      <li>555-702-1948
        <svg viewBox="0 0 24 24" aria-hidden="true"><rect x="5" y="2" width="14" height="20" rx="2.5" fill="none" stroke="var(--icon-ink)" stroke-width="1.8"/><circle cx="12" cy="18.5" r="1.2" fill="var(--icon-ink)"/></svg>
      </li>
      <li class="gap-before">mark@crisplaneglow.com
        <svg viewBox="0 0 24 24" aria-hidden="true"><circle cx="12" cy="12" r="10.5" fill="none" stroke="var(--icon-ink)" stroke-width="1.8"/><rect x="6.5" y="8" width="11" height="8" fill="none" stroke="var(--icon-ink)" stroke-width="1.5"/><path d="M6.5 8l5.5 4.5L17.5 8" fill="none" stroke="var(--icon-ink)" stroke-width="1.5"/></svg>
      </li>
      <li>www.crisplaneglow.com
        <svg viewBox="0 0 24 24" aria-hidden="true"><rect x="2" y="2" width="20" height="20" rx="4" fill="var(--icon-ink)"/><circle cx="12" cy="12" r="6.5" fill="none" stroke="#fff" stroke-width="1.5"/><path d="M5.5 12h13M12 5.5c-3 3.5-3 9.5 0 13M12 5.5c3 3.5 3 9.5 0 13" fill="none" stroke="#fff" stroke-width="1.3"/></svg>
      </li>
    </ul>

    <div class="accent-rule"></div>
    <p class="tagline">The complete carwash company</p>
    <p class="service-area">serving texas and oklahoma</p>
  </section>
</main>
</body>
</html>
```